Modern Innovative Business Card Design

We require a nice, modern, clean business card design, ready for upload to Cardwello. Our company develops online banking software solutions for small financial insitutions. The design should be clean, professional, but yet not "corporate boring". See www.fintrola.com for an idea of business image and profile. The design should communicate innovation, be modern and fresh, yet look professional and established.

Target Market(s)

Finance industry, bankers, entrepreneurs

Industry/Entity Type

Financial

Contact Information for Business Card

Daniel Hargreave
CEO

FINTROLA BV
Lindenhofstraat 38
1072 KD Amsterdam
The Netherlands

Phone: +31 20 517 8063
Direct: +31 20 446 1975
Skype: daniel.fintrola
ceo@fintrola.com
www.fintrola.com

Font styles to use
Sans Serif

Requirements
Must have
• Should look clean, modern and professional. File should be ready for upload to cardwello.
Should not have
• Boring standard corporate layout

```html
<!DOCTYPE html>
<html lang="en">
<head>
<meta charset="utf-8">
<title>FINTROLA business card</title>
<link href="https://fonts.googleapis.com/css2?family=Arimo:wght@400;700&display=swap" rel="stylesheet">
<style>
  :root {
    --bg: #e9e7e4;
    --white: #ffffff;
    --ink: #6b6c6e;
    --ink-dark: #4a4b4d;
    --green: #8cc63f;
    --band-dark: #58595b;
    --band-light: #9b9c9e;
    --back-dark: #505153;
    --back-light: #8a8b8d;
  }
  * { box-sizing: border-box; margin: 0; padding: 0; }
  html, body { width: 1200px; height: 914px; overflow: hidden; }
  body {
    background: var(--bg);
    font-family: "Arimo", Arial, sans-serif;
    color: var(--ink);
    position: relative;
  }
  .card {
    position: absolute;
    top: 283px;
    width: 540px;
    height: 348px;
    overflow: hidden;
    box-shadow: 0 8px 24px rgba(0,0,0,.18);
  }
  .card--front { left: 40px; background: var(--white); }
  .card--back {
    left: 620px;
    background: linear-gradient(135deg, var(--back-light), var(--back-dark));
    display: flex; align-items: center; justify-content: center;
  }

  .wordmark {
    display: flex; align-items: center; gap: 10px;
    font-weight: 400; font-size: 46px; letter-spacing: 4px; line-height: 1;
  }
  .wordmark__mark { width: 14px; height: 14px; background: var(--green); flex: none; }
  .card--front .wordmark { position: absolute; left: 34px; top: 36px; color: var(--ink); }
  .card--back .wordmark { color: var(--white); font-size: 50px; }

  .person { position: absolute; left: 38px; top: 106px; }
  .person__name { font-size: 18px; font-weight: 700; color: var(--ink); }
  .person__role { font-size: 12.5px; color: var(--green); margin-top: 3px; }

  .rule {
    position: absolute; left: 170px; right: 40px; top: 160px;
    height: 1px; background: var(--ink-dark);
  }

  .contact { position: absolute; list-style: none; font-size: 13px; line-height: 19px; color: var(--ink-dark); }
  .contact li { display: flex; align-items: center; gap: 8px; }
  .contact--phones { left: 38px; top: 184px; }
  .contact--address { left: 330px; top: 104px; }
  .contact--address li { align-items: flex-start; }
  .contact--online { left: 330px; top: 246px; }
  .icon {
    width: 13px; height: 13px; flex: none;
    background: var(--green);
    display: inline-flex; align-items: center; justify-content: center;
  }
  .icon svg { width: 9px; height: 9px; }
  .address-lines { display: block; }

  .band-line {
    position: absolute; left: 0; top: 292px; width: 214px; height: 5px;
    background: var(--band-dark);
  }
  .band-green {
    position: absolute; left: 0; top: 302px; width: 206px; height: 46px;
    background: var(--green);
  }
  .band-grey {
    position: absolute; left: 218px; right: 0; top: 292px; bottom: 0;
    background: linear-gradient(90deg, var(--band-dark), var(--band-light));
  }
</style>
</head>
<body>

<section class="card card--front" aria-label="Business card front">
  <div class="wordmark"><span class="wordmark__mark"></span>FINTROLA</div>

  <div class="person">
    <p class="person__name">Daniel Hargreave</p>
    <p class="person__role">CEO FINTROLA BV</p>
  </div>

  <div class="rule"></div>

  <ul class="contact contact--phones">
    <li><span class="icon"><svg viewBox="0 0 10 10"><rect x="2.5" y="1" width="5" height="8" rx="1" fill="#fff"/></svg></span>+31 20 446 1975</li>
    <li><span class="icon"><svg viewBox="0 0 10 10"><path d="M2 1l2 2-1 1.5c.6 1.2 1.3 1.9 2.5 2.5L7 6l2 2-1.5 1.5C4.5 9 1 5.5.5 2.5z" fill="#fff"/></svg></span>+31 20 517 8063</li>
    <li><span class="icon"><svg viewBox="0 0 10 10"><path d="M1 2h8v5H4L2 9V7H1z" fill="#fff"/></svg></span>daniel.fintrola</li>
  </ul>

  <ul class="contact contact--address">
    <li><span class="icon" style="margin-top:3px"><svg viewBox="0 0 10 10"><path d="M5 .5a3 3 0 0 1 3 3C8 6 5 9.5 5 9.5S2 6 2 3.5a3 3 0 0 1 3-3z" fill="#fff"/><circle cx="5" cy="3.5" r="1.1" fill="#8cc63f"/></svg></span>
      <span class="address-lines">Lindenhofstraat 38<br>1072 KD Amsterdam<br>The Netherlands</span></li>
  </ul>

  <ul class="contact contact--online">
    <li><span class="icon"><svg viewBox="0 0 10 10"><rect x="1" y="2" width="8" height="6" fill="#fff"/><path d="M1 2l4 3.5L9 2" stroke="#8cc63f" stroke-width="1" fill="none"/></svg></span>ceo@fintrola.com</li>
    <li><span class="icon"><svg viewBox="0 0 10 10"><circle cx="5" cy="5" r="3.8" fill="none" stroke="#fff" stroke-width="1.1"/><path d="M1.2 5h7.6M5 1.2c-2 2.5-2 5 0 7.6M5 1.2c2 2.5 2 5 0 7.6" stroke="#fff" stroke-width=".8" fill="none"/></svg></span>www.fintrola.com</li>
  </ul>

  <div class="band-line"></div>
  <div class="band-green"></div>
  <div class="band-grey"></div>
</section>

<section class="card card--back" aria-label="Business card back">
  <div class="wordmark"><span class="wordmark__mark"></span>FINTROLA</div>
</section>

</body>
</html>
```